House Builder and Property Development Card Design and Logo

I need a business card design for a building and property development company.
Colour scheme of Dark Grey and Green, I would like it bold, sharp and professional.
No logo yet done, I'm open to options but please stay away from the usual- house, roof, hammers etc.
Thanks Lou
Updates

Please be aware that on the business card information section the VKRT # 5382917 is a licence number and my phone number 0461739258. The numbers are close together and could be mistaken as one whole number 

Thank you

                                   

Industry/Entity Type

Building

Contact Information for Business Card

HARLOW BUILD & DEVELOPMENT.
Residential Building & Property Development
Louis Harlow - Director
VKRT # 5382917
0461739258
lou@harlowbuild.com.au

Requirements
Must have
• Bold Business name
Dark grey and green colours
Should not have
• roof outline or hammer logo

```html
<!DOCTYPE html>
<html lang="en">
<head>
<meta charset="utf-8">
<title>Harlow Build &amp; Development – Business Card</title>
<link href="https://fonts.googleapis.com/css2?family=Mulish:ital,wght@0,400;0,700;1,400&family=Pinyon+Script&display=swap" rel="stylesheet">
<style>
  :root {
    --green: #62a547;
    --grey-dark: #4b4b4d;
    --grey-text: #4a4a4c;
    --paper: #ffffff;
    --white: #ffffff;
  }
  * { margin: 0; padding: 0; box-sizing: border-box; }
  html, body {
    width: 1200px;
    height: 742px;
    overflow: hidden;
    background: var(--paper);
  }
  .card {
    position: relative;
    width: 1200px;
    height: 742px;
    background: var(--paper);
    font-family: "Mulish", sans-serif;
  }
  .person {
    position: absolute;
    right: 104px;
    top: 78px;
    text-align: right;
  }
  .person-name {
    font-weight: 400;
    font-size: 45px;
    color: var(--green);
    line-height: 1;
    letter-spacing: 0.5px;
  }
  .person-role {
    font-family: "Pinyon Script", cursive;
    font-size: 34px;
    color: var(--grey-text);
    line-height: 1;
    margin-top: 8px;
    margin-right: 8px;
  }
  .brand-art {
    position: absolute;
    left: 96px;
    top: 217px;
    width: 206px;
    height: 330px;
    background: linear-gradient(90deg, #8cc26e 0%, #7fb862 35%, #5a5a5c 45%, #3f3f41 100%);
  }
  .company-name {
    position: absolute;
    left: 322px;
    top: 472px;
    font-weight: 700;
    font-size: 64px;
    line-height: 1;
    color: var(--grey-text);
    letter-spacing: -0.5px;
    white-space: nowrap;
  }
  .rule {
    position: absolute;
    left: 73px;
    top: 549px;
    width: 1052px;
    height: 4px;
    background: var(--green);
  }
  .tagline {
    position: absolute;
    left: 138px;
    top: 555px;
    font-family: "Pinyon Script", cursive;
    font-size: 44px;
    line-height: 1.2;
    color: var(--grey-text);
    white-space: nowrap;
  }
  .contact-bar {
    position: absolute;
    left: 73px;
    top: 631px;
    width: 1050px;
    height: 56px;
    background: var(--grey-dark);
    display: flex;
    align-items: center;
    justify-content: space-between;
    padding: 0 19px 0 21px;
    color: var(--white);
    font-style: italic;
    font-size: 31px;
    letter-spacing: 0.5px;
    white-space: nowrap;
  }
</style>
</head>
<body>
  <main class="card">
    <header class="person">
      <p class="person-name">Louis Harlow</p>
      <p class="person-role">Director</p>
    </header>

    <div class="brand-art" role="img" aria-label="Illustration of green and dark grey high-rise towers"></div>

    <h1 class="company-name">Harlow Build &amp; Development</h1>
    <div class="rule"></div>
    <p class="tagline">Residential Building &amp; Property Development</p>

    <footer class="contact-bar">
      <span class="contact-licence">VKRT # 5382917 0461739258</span>
      <span class="contact-email">lou@harlowbuild.com.au</span>
    </footer>
  </main>
</body>
</html>
```